A Label for an ECO Friendly Spirit Company

Design a label which can be used for vodka and gin (London Dry Gin). It should be Square type Like the Shape File you see in the uploads. VORK means Local Eco friendly Authentic and Fair. We want a cool and slim label that calls for eco-friendly. We want to use it for our premium
Vodka and our London Dry Gin. Please use the logo and design it in Square Type.

40%vol, 700ml

Target Market(s)

spirits and events

Industry/Entity Type

SPIRITS

Colors
00AB8E
00BBA5
67D7C9
C6EFE9
E9F9F6
59FF00
82FF00
B8FF75
E3FFCB
F4FFEA

Requirements
Must have
• Logo from VORK, Squaee Shape

```html
<!DOCTYPE html>
<html lang="en">
<head>
<meta charset="utf-8">
<title>VORK London Dry Gin – Label Variants</title>
<link rel="stylesheet" href="https://fonts.googleapis.com/css2?family=Montserrat:wght@300;400;600&display=swap">
<style>
  :root {
    --page-bg: #ffffff;
    --leaf-green: #8cc63f;
    --band-white: #ffffff;
    --label-black: #231f20;
    --label-teal: #00ab8e;
    --rule-teal: #00bba5;
    --ink-white: #ffffff;
  }
  html, body {
    margin: 0;
    padding: 0;
    width: 1000px;
    height: 1200px;
    overflow: hidden;
    background: var(--page-bg);
  }
  .label-sheet {
    position: relative;
    width: 1000px;
    height: 1200px;
    display: flex;
    justify-content: space-around;
    align-items: center;
    padding: 0 20px;
    box-sizing: border-box;
  }
  .gin-label {
    width: 460px;
    height: 460px;
    display: block;
  }
  .gin-label .frame-outer { fill: var(--leaf-green); }
  .gin-label .frame-band { fill: var(--band-white); }
  .gin-label--night .label-field { fill: var(--label-black); }
  .gin-label--lagoon .label-field { fill: var(--label-teal); }
  .gin-label--night .inner-rule { stroke: var(--rule-teal); }
  .gin-label--lagoon .inner-rule { stroke: var(--ink-white); }
  .inner-rule { fill: none; stroke-width: 1.2; }
  .brand-mark { fill: var(--ink-white); }
  .brand-name {
    font-family: "Montserrat", sans-serif;
    font-weight: 600;
    font-size: 22px;
    fill: var(--ink-white);
  }
  .product-title {
    font-family: "Montserrat", sans-serif;
    font-weight: 300;
    font-size: 47px;
    fill: var(--ink-white);
  }
  .spec-strength {
    font-family: "Montserrat", sans-serif;
    font-weight: 400;
    font-size: 15px;
    fill: var(--ink-white);
  }
  .spec-volume {
    font-family: "Montserrat", sans-serif;
    font-weight: 400;
    font-size: 11px;
    fill: var(--ink-white);
  }
</style>
</head>
<body>
  <main class="label-sheet">
    <svg class="gin-label gin-label--night" viewBox="0 0 460 460" aria-label="VORK London Dry Gin label, black edition">
      <polygon class="frame-outer" points="230,0 460,230 230,460 0,230"/>
      <polygon class="frame-band" points="230,33 427,230 230,427 33,230"/>
      <polygon class="label-field" points="230,50 410,230 230,410 50,230"/>
      <polygon class="inner-rule" points="230,63 397,230 230,397 63,230"/>
      <rect class="brand-mark" x="221" y="84" width="18" height="18"/>
      <text class="brand-name" x="230" y="127" text-anchor="middle">VORK</text>
      <text class="product-title" x="230" y="226" text-anchor="middle" textLength="238" lengthAdjust="spacing">LONDON</text>
      <text class="product-title" x="230" y="270" text-anchor="middle" textLength="238" lengthAdjust="spacing">DRY GIN</text>
      <text class="spec-strength" x="230" y="353" text-anchor="middle">40%vol</text>
      <text class="spec-volume" x="230" y="369" text-anchor="middle">700ml</text>
    </svg>

    <svg class="gin-label gin-label--lagoon" viewBox="0 0 460 460" aria-label="VORK London Dry Gin label, teal edition">
      <polygon class="frame-outer" points="230,0 460,230 230,460 0,230"/>
      <polygon class="frame-band" points="230,33 427,230 230,427 33,230"/>
      <polygon class="label-field" points="230,50 410,230 230,410 50,230"/>
      <polygon class="inner-rule" points="230,63 397,230 230,397 63,230"/>
      <rect class="brand-mark" x="221" y="84" width="18" height="18"/>
      <text class="brand-name" x="230" y="127" text-anchor="middle">VORK</text>
      <text class="product-title" x="230" y="226" text-anchor="middle" textLength="238" lengthAdjust="spacing">LONDON</text>
      <text class="product-title" x="230" y="270" text-anchor="middle" textLength="238" lengthAdjust="spacing">DRY GIN</text>
      <text class="spec-strength" x="230" y="351" text-anchor="middle">40%vol</text>
      <text class="spec-volume" x="230" y="367" text-anchor="middle">700ml</text>
    </svg>
  </main>
</body>
</html>
```